lawn sign

we need a design for our organic mosquito spray service. should fit a 27in x 18in yard sign. Includes our company logo and a picture of a mosquito with a circle around it crossed out (example included).

It needs to be simple, easily readable and in clear resolution. Signs needs to include the text: "this lawn receives ORGANIC treatments for mosquitoes and chiggers. Instantly SAFE for people and pets".

Include our phone number and website "615-372-5810" "yardvelnor.example"

our ideas are: organic = no pests (use example pic)
no chemicals used = safe

Reason: we have been too busy to look at all of the designs. we will look at them all in the next day. thank you for your efforts and creativity!

```html
<!DOCTYPE html>
<html lang="en">
<head>
<meta charset="utf-8">
<title>Yardvelnor Lawn Sign</title>
<link href="https://fonts.googleapis.com/css2?family=Raleway:wght@200;300;500;600;800;900&display=swap" rel="stylesheet">
<style>
  :root {
    --backdrop: #d9676b;
    --sign-face: #e27b7d;
    --sign-edge: #eb9597;
    --ink: #ffffff;
    --ink-soft: rgba(255, 255, 255, 0.85);
    --mark-fill: rgba(255, 255, 255, 0.35);
  }
  * { box-sizing: border-box; margin: 0; padding: 0; }
  html, body {
    width: 1200px;
    height: 1000px;
    overflow: hidden;
    background: var(--backdrop);
    font-family: "Raleway", sans-serif;
    color: var(--ink);
  }
  .canvas {
    width: 1200px;
    height: 1000px;
    display: flex;
    align-items: center;
    justify-content: center;
  }
  .yard-sign {
    width: 540px;
    height: 920px;
    background: var(--sign-face);
    border: 1px solid var(--sign-edge);
    display: flex;
    flex-direction: column;
    align-items: center;
    padding: 80px 50px 50px;
  }
  .brand {
    text-align: center;
    margin-bottom: 44px;
  }
  .brand-name {
    font-size: 36px;
    font-weight: 500;
    letter-spacing: 0.5px;
    line-height: 1;
  }
  .no-pest-icon {
    width: 170px;
    height: 170px;
    margin-bottom: 40px;
  }
  .rule {
    width: 100%;
    height: 1.5px;
    background: var(--ink-soft);
  }
  .message {
    text-align: center;
    padding: 22px 0 18px;
    line-height: 1.05;
  }
  .message-intro { font-size: 46px; font-weight: 200; }
  .message-organic { font-size: 82px; font-weight: 900; letter-spacing: 1px; }
  .message-treatments { font-size: 55px; font-weight: 800; }
  .message-pests { font-size: 50px; font-weight: 600; }
  .message-safe { font-size: 50px; font-weight: 300; }
  .message-audience { font-size: 40px; font-weight: 200; }
  .contact {
    margin-top: 22px;
    font-size: 16px;
    font-weight: 500;
    letter-spacing: 0.3px;
  }
  .contact .dot { margin: 0 6px; }
</style>
</head>
<body>
<main class="canvas">
  <section class="yard-sign">
    <header class="brand">
      <div class="brand-name">Yardvelnor</div>
    </header>

    <svg class="no-pest-icon" viewBox="0 0 170 170">
      <circle cx="85" cy="85" r="82" fill="none" stroke="#ffffff" stroke-width="2"/>
      <circle cx="85" cy="85" r="48" fill="var(--mark-fill)" role="img" aria-label="Mosquito silhouette"/>
      <line x1="27" y1="143" x2="143" y2="27" stroke="#ffffff" stroke-width="2"/>
    </svg>

    <div class="rule"></div>

    <div class="message">
      <div class="message-intro">this lawn receives</div>
      <div class="message-organic">ORGANIC</div>
      <div class="message-treatments">TREATMENTS</div>
      <div class="message-pests">for mosquitoes</div>
      <div class="message-pests">and chiggers.</div>
      <div class="message-safe">Instantly SAFE</div>
      <div class="message-audience">for people and pets</div>
    </div>

    <div class="rule"></div>

    <footer class="contact">615-372-5810<span class="dot">•</span>www.yardvelnor.example</footer>
  </section>
</main>
</body>
</html>
```